Business Card for Fashion House

We need a business card design for our personalize fashion service for our customers. the business card should reflect reliability, luxury and creativity.
The brand Gravetto is extracted from "Graceful Vetto"; Gravetto provides fashion designs sprinkled with luxury and style tailored for our elite clients character profile.
Gravetto is created for those who embody class and elegance with a passion for style.
Target Market(s)
Affluent Customers
Industry/Entity Type
Fashion
Contact Information for Business Card
Rania Bou Khalil
Fashion Designer
Telephone: +971 5550123
Mobile +971 555987
Emal q@z.com
Website www.gravetto-example.com
Social Media Youtube g+ Facebook Instagram Pin /gravetto
Font styles to use
Other font styles liked:
- Audrey provided
Look and feel
Each slider illustrates characteristics of the customer's brand and the style your logo design should communicate.

```html
<!DOCTYPE html>
<html lang="en">
<head>
<meta charset="utf-8">
<title>Gravetto Business Card</title>
<link href="https://fonts.googleapis.com/css2?family=Marcellus&family=Montserrat:wght@400&display=swap" rel="stylesheet">
<style>
  :root {
    --page-bg: #2a2a2a;
    --card-light: #ffffff;
    --card-dark: #1c1c1c;
    --ink: #222222;
    --ink-soft: #3a3a3a;
    --paper-ink: #ffffff;
    --shadow: rgba(0, 0, 0, 0.55);
  }
  * { margin: 0; padding: 0; box-sizing: border-box; }
  html, body {
    width: 1200px;
    height: 897px;
    overflow: hidden;
    background: var(--page-bg);
  }
  .canvas {
    position: relative;
    width: 1200px;
    height: 897px;
  }
  .card {
    position: absolute;
    left: 303px;
    width: 595px;
    height: 338px;
    box-shadow: 0 6px 18px var(--shadow);
  }
  .card--front { top: 92px; background: var(--card-light); color: var(--ink); }
  .card--back { top: 470px; background: var(--card-dark); color: var(--paper-ink); }

  .brand-mark {
    position: absolute;
    width: 60px;
    height: 60px;
    border-radius: 50%;
    border: 3px solid currentColor;
  }
  .card--front .brand-mark { left: 125px; top: 47px; }
  .card--back .brand-mark { left: 267px; top: 92px; }

  .wordmark {
    position: absolute;
    font-family: "Marcellus", serif;
    font-size: 29px;
    letter-spacing: 0.42em;
    line-height: 1;
    white-space: nowrap;
  }
  .card--front .wordmark { left: 39px; top: 144px; }
  .card--back .wordmark {
    left: 0; right: 0; top: 224px;
    text-align: center;
    padding-left: 0.42em;
  }

  .holder-name {
    position: absolute;
    left: 39px; top: 226px;
    font-family: "Marcellus", serif;
    font-size: 19px;
    letter-spacing: 0.04em;
  }
  .holder-role {
    position: absolute;
    left: 39px; top: 253px;
    font-family: "Montserrat", sans-serif;
    font-size: 13px;
    color: var(--ink-soft);
  }
  .divider {
    position: absolute;
    left: 39px; top: 279px;
    width: 518px;
    height: 1.5px;
    background: var(--ink);
  }
  .contact-line {
    position: absolute;
    left: 39px; top: 292px;
    font-family: "Montserrat", sans-serif;
    font-size: 11.4px;
    color: var(--ink-soft);
    white-space: nowrap;
  }
  .social-handle {
    position: absolute;
    left: 0; right: 0; top: 290px;
    text-align: center;
    font-family: "Montserrat", sans-serif;
    font-size: 17px;
    letter-spacing: 0.05em;
  }
</style>
</head>
<body>
<main class="canvas">
  <section class="card card--front" aria-label="Card front">
    <span class="brand-mark" aria-hidden="true"></span>
    <div class="wordmark">GRAVETTO</div>
    <div class="holder-name">RANIA BOU KHALIL</div>
    <div class="holder-role">Fashion Designer</div>
    <div class="divider"></div>
    <div class="contact-line">Phn: +971 5550123 | Cell: +971 555987 | Email: q@z.com | www.gravetto-example.com</div>
  </section>

  <section class="card card--back" aria-label="Card back">
    <span class="brand-mark" aria-hidden="true"></span>
    <div class="wordmark">GRAVETTO</div>
    <div class="social-handle">/gravetto</div>
  </section>
</main>
</body>
</html>
```